Simple and Approachable Cover for Pet Expo Company Page

Size: 2000 x 430; looking simply for words "Dunmore HR Consulting" and email address "DunmoreHRConsulting@brelvamail.com." This is for a cover photo for a company profile page for the Hollow Oak Expo, where I am a featured speaker on Employee Communications later this month. You can incorporate the attached photo to the left of the banner ad if you wish. The mood I wish to present is approachable, positive and simple.

Target Market(s)

small pet retail business owners

Industry/Entity Type

Pet Shop

Font styles to use
Serif
Sans Serif

Requirements
Must have
• Email address clearly defined/separated. Easy to read.
Nice to have
• I like the picture that I included; subtle pet paw background is also nice
Should not have
• No paid stock images

```html
<!DOCTYPE html>
<html lang="en">
<head>
<meta charset="UTF-8">
<title>Dunmore HR Consulting – Cover</title>
<link rel="stylesheet" href="https://fonts.googleapis.com/css2?family=Poppins:ital,wght@0,800;1,700;1,800&display=swap">
<style>
  :root {
    --page: #ffffff;
    --orange: #f6a727;
    --navy: #1d3f86;
    --band: #2f86cf;
    --white: #ffffff;
    --shadow: #c9c9c9;
    --grass: #7d9a4e;
    --shirt-red: #d9524a;
    --denim: #5f7fa6;
    --hound-tan: #c98a4c;
    --dog-tan: #b86a32;
    --dog-white: #f3eee8;
  }
  * { margin: 0; padding: 0; box-sizing: border-box; }
  html, body {
    width: 1200px; height: 1200px; overflow: hidden;
    background: var(--page);
  }
  .cover {
    position: absolute;
    left: 0; top: 471px;
    width: 1200px; height: 258px;
    background: var(--orange);
    overflow: hidden;
    font-family: "Poppins", sans-serif;
  }
  .team-photo {
    position: absolute; left: 0; top: 0;
    width: 380px; height: 258px;
    background:
      radial-gradient(ellipse 70px 90px at 225px 110px, rgba(217,82,74,0.75), rgba(217,82,74,0) 100%),
      radial-gradient(ellipse 70px 60px at 90px 140px, rgba(201,138,76,0.8), rgba(201,138,76,0) 100%),
      radial-gradient(ellipse 90px 50px at 200px 205px, rgba(95,127,166,0.7), rgba(95,127,166,0) 100%),
      linear-gradient(180deg, #8a9a6a 0%, #a89a72 45%, var(--grass) 100%);
    -webkit-mask-image: linear-gradient(90deg, #000 0%, #000 70%, transparent 100%);
    mask-image: linear-gradient(90deg, #000 0%, #000 70%, transparent 100%);
  }
  .corner-shape {
    position: absolute; left: 0; top: 0;
    width: 104px; height: 72px;
  }
  .dog-photo {
    position: absolute; right: 0; top: 0;
    width: 260px; height: 258px;
    background:
      radial-gradient(ellipse 70px 80px at 170px 150px, var(--dog-white) 0%, rgba(243,238,232,0.9) 50%, rgba(243,238,232,0) 100%),
      radial-gradient(ellipse 90px 140px at 175px 120px, var(--dog-tan) 0%, rgba(184,106,50,0.6) 55%, rgba(184,106,50,0) 100%),
      radial-gradient(ellipse 80px 90px at 230px 240px, var(--dog-white) 0%, rgba(243,238,232,0) 100%);
  }
  .email-band {
    position: absolute; left: 230px; top: 207px;
    width: 880px; height: 38px;
    background: linear-gradient(90deg, rgba(47,134,207,0) 0%, var(--band) 12%, var(--band) 100%);
  }
  .name {
    position: absolute; left: 266px; top: 4px;
    font-style: italic; font-weight: 800;
    font-size: 110px; line-height: 140px;
    color: var(--white);
    letter-spacing: -2px;
    text-shadow: 4px 4px 0 var(--shadow);
    white-space: nowrap;
  }
  .tagline {
    position: absolute; left: 308px; top: 118px;
    font-weight: 800;
    font-size: 82px; line-height: 100px;
    color: var(--navy);
    letter-spacing: 3px;
    text-shadow: 3px 3px 0 var(--white);
    white-space: nowrap;
  }
  .email {
    position: absolute; left: 330px; top: 207px;
    font-style: italic; font-weight: 700;
    font-size: 25px; line-height: 38px;
    color: var(--white);
    white-space: nowrap;
  }
</style>
</head>
<body>
  <section class="cover">
    <div class="team-photo" role="img" aria-label="Photo of the two consultants kneeling on grass with their two hound dogs"></div>
    <svg class="corner-shape" viewBox="0 0 104 72" aria-hidden="true">
      <path d="M0 0 H104 C80 6 78 30 60 48 C44 64 20 66 0 72 Z" fill="#1d3f86"/>
    </svg>
    <div class="dog-photo" role="img" aria-label="Photo of a brown and white terrier in profile wearing a leather collar"></div>
    <div class="email-band"></div>
    <h1 class="name">Dunmore HR</h1>
    <p class="tagline">CONSULTING</p>
    <p class="email">DunmoreHRConsulting@brelvamail.com</p>
  </section>
</body>
</html>
```